Brisk-up-ward ... The new business framework that makes Accountability work!

We need a book cover for the next version of Accountability that business uses to maximize productivity and profits. Being Brisk-up-ward empowers the employee and enables the employer to ensure they have the right person in the right position taking on the right priorities.

The final design should exude confidence and simplicity. It should embrace trust, alignment of goals and teams working well together.

Please review the slide presentation for details about the Pivot - Harbor Framework which is a key component of the program. I'd like to see how the cover can simply have people be connected to this concept.

https://slides.vantorelhub.com/deck/d/7qRmT2vLpXe8NwZc41sKjHbY63DfuGa9PQ20o_VbXs/view?mode=share

Please see www.marnoquillhall.com for more on the program which is called Blue Orbit 40.

I'd like to incorporate my headshot on the back of the book cover. I'm trying to figure out how to upload it. Please make a placeholder for it in the design or if I've figured out how to upload it please use it.

I'm expecting my new headshot to be done in 3-4 days and will need this to finalize the design. I would like another 5 days.

Target Market(s)

CEO's and Business owners of businesses with 50 to 500 employees

Industry/Entity Type

Small and Medium businesses

Font styles to use
Sans Serif
Other font styles liked:
• Ariel, Raleway

Colors
0054AA
0677BA
7BADD7
CADEEF
E8F1F8
0094D4
00A9DD
6FCCEA
C7EBF8
E9F6FB
00AB8E
00BBA5
67D7C9
C6EFE9
E9F9F6

Requirements
Must have
• a graphic that has people think simplicity, trust, and be counted on
Nice to have
• images of a person and place people can count on. Maybe a superhero, maybe a team working together
Should not have
• religious or political symbols

```html
<!DOCTYPE html>
<html lang="en">
<head>
<meta charset="utf-8">
<title>Brisk Up Ward – Book Cover</title>
<link rel="stylesheet" href="https://fonts.googleapis.com/css2?family=Montserrat:wght@400;600;700&display=swap">
<style>
  :root {
    --cover-top: #2e3a4e;
    --cover-mid: #283244;
    --cover-bottom: #1c2331;
    --hero-light: #9fb4cc;
    --hero-mid: #5f7896;
    --hero-suit: #3a4a62;
    --hero-edge: #2b3649;
    --title-white: #f2f2f2;
    --title-blue: #7aa8d4;
    --subtitle: #c9d7e6;
    --author: #f4f4f4;
  }
  * { margin: 0; padding: 0; box-sizing: border-box; }
  html, body {
    width: 991px;
    height: 1200px;
    overflow: hidden;
    background: #ffffff;
  }
  .cover {
    position: relative;
    width: 991px;
    height: 1200px;
    background: linear-gradient(180deg, var(--cover-top) 0%, var(--cover-mid) 55%, var(--cover-bottom) 100%);
    font-family: "Montserrat", Arial, sans-serif;
    overflow: hidden;
  }
  .hero-art {
    position: absolute;
    left: 0;
    top: 0;
    width: 991px;
    height: 620px;
    background:
      radial-gradient(ellipse 20% 26% at 50% 30%, var(--hero-light) 0%, rgba(159,180,204,0.55) 45%, rgba(95,120,150,0) 100%),
      radial-gradient(ellipse 26% 12% at 50% 56%, rgba(201,170,150,0.55) 0%, rgba(201,170,150,0) 100%),
      radial-gradient(ellipse 42% 60% at 50% 42%, var(--hero-mid) 0%, var(--hero-suit) 60%, var(--hero-edge) 100%);
    -webkit-mask-image: linear-gradient(180deg, #000 0%, #000 80%, transparent 100%);
    mask-image: linear-gradient(180deg, #000 0%, #000 80%, transparent 100%);
  }
  .title {
    position: absolute;
    left: 0;
    right: 0;
    top: 598px;
    text-align: center;
    line-height: 1;
  }
  .title-line {
    display: block;
    font-size: 122px;
    font-weight: 400;
    color: var(--title-white);
    letter-spacing: 1px;
    height: 112px;
  }
  .title-line--accent {
    font-weight: 700;
    color: var(--title-blue);
  }
  .subtitle {
    position: absolute;
    left: 0;
    right: 0;
    top: 985px;
    text-align: center;
    font-size: 32px;
    font-weight: 600;
    line-height: 1.3;
    letter-spacing: 1.2px;
    color: var(--subtitle);
  }
  .author {
    position: absolute;
    left: 0;
    right: 0;
    top: 1120px;
    text-align: center;
    font-size: 34px;
    font-weight: 700;
    letter-spacing: 8px;
    color: var(--author);
  }
</style>
</head>
<body>
  <main class="cover">
    <div class="hero-art" role="img" aria-label="Photo placeholder: businessman in a dark suit holding open cupped hands, with a small team of light blue figures standing on them, a leader in front"></div>
    <h1 class="title">
      <span class="title-line">BRISK</span>
      <span class="title-line">UP</span>
      <span class="title-line title-line--accent">WARD</span>
    </h1>
    <p class="subtitle">The new business framework that<br>makes Accountability work!</p>
    <p class="author">DANA PRESTWICK</p>
  </main>
</body>
</html>
```